New Pump Website Design Needed

We need a homepage concept for a pump website rebuild.

The navigation at the top must be:
Home - About Us - Pump Stations - Pumps - Electrical - Drainage - Environmental - Accessories - Contact Us

The homepage should have the the following structure:
Logo
Navigation
Rotating Banner
Content + Picture of PDF Flipbook to download/ view
Featured Products (in one row - approx 4)
Footer

The footer must include:
Left side - navigation small.
"Copyright RiverWell 2014. All Rights reserved"

Right side: "Website by Pagecraft Studio"

Content and imagery, and Logo can be taken from their existing website: tidelinehydro.co.nz

We have attached a copy of their New PDF - the new website design must reflect this (Use block colours/ different colours for the navigation items/ incorporate the footer image).

Industry/Entity Type

Electrical

Font styles to use
Sans Serif

Requirements
Must have
• Features from their brochure brought in (colour scheme and footer feature)
Should not have
• Any Social Media Icons

```html
<!DOCTYPE html>
<html lang="en">
<head>
<meta charset="utf-8">
<title>RiverWell Pump Systems</title>
<link href="https://fonts.googleapis.com/css2?family=Oxygen:wght@400;700&family=Arimo:wght@400;700&family=Open+Sans:wght@400;600&display=swap" rel="stylesheet">
<style>
:root{
  --ink:#1b1b1b;
  --nav:#262626;
  --red:#c8101a;
  --blue:#0a5aa6;
  --text:#333;
  --green:#18a07a;
  --lime:#86b00e;
  --gold:#e0b20a;
  --footer:#1f1f1f;
  --footer-bar:#111;
}
*{margin:0;padding:0;box-sizing:border-box}
html,body{width:995px;height:1200px;overflow:hidden;background:#fff}
body{position:relative;font-family:Arimo,Arial,sans-serif;color:var(--text)}
.abs{position:absolute}

.brand{left:83px;top:26px;display:flex;align-items:center;gap:10px}
.brand-mark{width:34px;height:34px;background:var(--blue)}
.brand-name{font-family:Oxygen,sans-serif;font-weight:700;font-size:30px;color:var(--ink);letter-spacing:1px}

.call{left:587px;top:36px;display:flex;align-items:center;gap:6px;font-family:"Open Sans",sans-serif;font-size:21px}
.call .label{color:#2a8fc6}
.call .num{color:#444}
.live-chat{left:831px;top:38px;width:79px;height:22px;background:#6ab22c;color:#fff;font-family:Oxygen,sans-serif;font-weight:700;font-size:11.5px;line-height:22px;text-align:center}
.live-chat::after{content:"";position:absolute;left:10px;bottom:-6px;border-left:6px solid #6ab22c;border-bottom:6px solid transparent}

.nav{left:0;top:99px;width:995px;height:40px;background:var(--nav)}
.nav-list{position:absolute;left:84px;top:0;width:828px;height:40px;display:flex;justify-content:space-between;align-items:center;list-style:none}
.nav-list li{display:flex;align-items:center;height:40px}
.nav-list a{color:#fff;font-family:Oxygen,sans-serif;font-weight:700;font-size:11px;text-decoration:none;white-space:nowrap}
.nav-list a.active{display:block;width:66px;height:29px;line-height:29px;text-align:center;background:var(--red);border-radius:4px}
.nav-list .sep{width:1px;height:28px;background:#444}

.banner{left:0;top:138px;width:995px;height:267px;background:linear-gradient(#16a3d3,#2cb2df 70%,#1b9fcd)}
.lower-fade{left:0;top:405px;width:995px;height:150px;background:linear-gradient(#e9eaeb,#fff)}
.slide{border-radius:50%;border:6px solid #f1f1f1;box-shadow:0 10px 14px rgba(0,0,0,.22)}
.arrow{top:292px;color:#d9f1fa;font-size:56px;font-family:Arimo,sans-serif;line-height:1}

.welcome{left:85px;top:470px;font-family:Oxygen,sans-serif}
.welcome h1{font-size:30px;font-weight:700;color:var(--blue);letter-spacing:.5px;line-height:34px}
.welcome h2{font-size:25px;font-weight:400;color:#111;letter-spacing:1.5px;line-height:34px}
.download{left:674px;top:473px;width:238px;height:64px;border-radius:5px;background:linear-gradient(#f2cf3a,#d9a80c);border:1px solid #c99a08}
.download b{position:absolute;left:22px;top:7px;font-size:27px;letter-spacing:1.5px;color:#111}
.download span{position:absolute;right:20px;top:36px;font-size:19px;color:#fff}
.rule{left:85px;top:552px;width:827px;border-top:1px dashed #b5b5b5}

.intro-photo{left:85px;top:572px;width:180px;height:159px;background:linear-gradient(135deg,#b9a98a,#6d7f96 55%,#2e5aa8)}
.intro-text{left:276px;top:570px;width:638px;font-size:11px;line-height:16.6px;color:#333}
.intro-text p+p{margin-top:16.6px}

.card{width:236px;height:262px;top:784px;background:#fff;border:1px solid #ddd;border-radius:4px;box-shadow:0 3px 3px rgba(0,0,0,.15)}
.ribbon{position:absolute;left:-7px;width:250px;height:32px;color:#fff;font-family:Oxygen,sans-serif;font-size:18px;line-height:32px;text-align:center;letter-spacing:.5px;border-radius:3px 3px 0 0}
.ribbon::before,.ribbon::after{content:"";position:absolute;top:-6px;width:7px;height:10px;filter:brightness(.6);background:inherit}
.ribbon::before{left:0;border-radius:3px 0 0 0}
.ribbon::after{right:0;top:auto;bottom:-6px}
.card .pic{position:absolute;left:10px;width:216px;height:90px}
.card p{position:absolute;left:10px;width:216px;text-align:center;font-size:10px;line-height:15px;color:#333}
.card .more{position:absolute;left:70px;width:92px;height:25px;background:var(--blue);border-radius:2px;color:#fff;font-size:13px;line-height:25px;text-align:center}

.footer{left:0;top:1088px;width:995px;height:85px;background:var(--footer)}
.vline{top:1102px;height:62px;border-left:1px dotted #555}
.foot-links{left:85px;top:1114px;width:560px;text-align:left;color:#fff;font-size:10px;line-height:23px}
.foot-brand{left:728px;top:1118px;display:flex;align-items:center;gap:8px}
.foot-brand .brand-mark{width:26px;height:26px;background:#bbb}
.foot-brand .brand-name{font-size:24px;color:#fff}
.footer-bar{left:0;top:1173px;width:995px;height:27px;background:var(--footer-bar);color:#eee;font-size:10px;line-height:27px}
.footer-bar .copy{position:absolute;left:85px}
.footer-bar .credit{position:absolute;right:83px}
</style>
</head>
<body>

<div class="abs brand"><span class="brand-mark"></span><span class="brand-name">RIVERWELL</span></div>

<div class="abs call">
  <svg width="22" height="22" viewBox="0 0 24 24" aria-hidden="true"><path d="M6.6 10.8a15 15 0 0 0 6.6 6.6l2.2-2.2c.3-.3.7-.4 1-.2 1.1.4 2.3.6 3.6.6.6 0 1 .4 1 1V20c0 .6-.4 1-1 1A17 17 0 0 1 3 4c0-.6.4-1 1-1h3.5c.6 0 1 .4 1 1 0 1.3.2 2.5.6 3.6.1.3 0 .7-.2 1z" fill="#c8101a"/><path d="M15 3h6v6M21 3l-6 6" stroke="#c8101a" stroke-width="2" fill="none"/></svg>
  <span class="label">call us:</span><span class="num">0800 742 618</span>
</div>
<div class="abs live-chat">LIVE CHAT</div>

<nav class="abs nav">
  <ul class="nav-list">
    <li><a class="active" href="#">HOME</a></li>
    <li class="sep"></li>
    <li><a href="#">ABOUT US</a></li>
    <li class="sep"></li>
    <li><a href="#">PUMP STATIONS</a></li>
    <li class="sep"></li>
    <li><a href="#">PUMPS</a></li>
    <li class="sep"></li>
    <li><a href="#">ELECTRICAL</a></li>
    <li class="sep"></li>
    <li><a href="#">DRAINAGE</a></li>
    <li class="sep"></li>
    <li><a href="#">ENVIRONMENTAL</a></li>
    <li class="sep"></li>
    <li><a href="#">ACCESSORIES</a></li>
    <li class="sep"></li>
    <li><a href="#">CONTACT US</a></li>
  </ul>
</nav>

<div class="abs banner"></div>
<div class="abs lower-fade"></div>
<div class="abs arrow" style="left:132px">&#10094;</div>
<div class="abs arrow" style="left:846px">&#10095;</div>
<div class="abs slide" role="img" aria-label="Blue industrial pumps in a plant room" style="left:193px;top:210px;width:194px;height:194px;background:radial-gradient(circle at 40% 45%,#3f6fd0,#1d3f96 60%,#6c86a8)"></div>
<div class="abs slide" role="img" aria-label="Plant seedling held in cupped hands" style="left:580px;top:197px;width:220px;height:220px;background:radial-gradient(circle at 50% 50%,#9ad43a,#4f9a12 70%,#2f6d08)"></div>
<div class="abs slide" role="img" aria-label="Worker beside a large pipeline section and excavator" style="left:367px;top:191px;width:256px;height:256px;background:linear-gradient(160deg,#8fa86a,#c8b34a 45%,#7ab3c9 70%,#3a3f45)"></div>

<div class="abs welcome"><h1>WELCOME TO</h1><h2>RiverWell Pump Systems</h2></div>
<div class="abs download"><b>DOWNLOAD</b><span>Our Product Guide</span></div>
<div class="abs rule"></div>

<div class="abs intro-photo" role="img" aria-label="Technician assembling a vertical pump on site"></div>
<div class="abs intro-text">
  <p>Lorem ipsum dolor sit amet, consectetur adipiscing elit. Quisque dapibus accumsan orci, pretium eleifend arcu adipiscing eget. Fusce accumsan facilisis tincidunt. Phasellus tempor enim purus, vitae venenatis est. Ut imperdiet hendrerit pulvinar. Cras at tellus a enim condimentum mollis ut et tellus. Mauris dolor magna, elementum eu dictum eu, fermentum a nibh. Praesent ut accumsan facilisis tincidunt. Phasellus tempor enim purus, vitae venenatis est. Ut imperdiet hendrerit pulvinar. Cras at tellus a enim condimentum mollis ut et tellus. Mauris dolor magna, elementum eu dictum dui lectus, vel lacinia sem. Praesent commo-do malesuada urna, quis convallis risus dictum et.</p>
  <p>Nunc dapibus interdum libero, et semper eros auctor ac. simply dummy text of the printing and typesetting industry. Lorem Ipsum has been the industry's standard dummy text ever since the 1500s, when an unknown printer took a galley of type and scrambled it to make a type specimen book. It has survived not only five centuries,</p>
</div>

<div class="abs card" style="left:91px">
  <div class="ribbon" style="top:16px;background:var(--green)">ENVIRONMENT</div>
  <div class="pic" role="img" aria-label="Pipeline section in a mountain valley" style="top:58px;background:linear-gradient(#8fb7d6,#6f8d5a 50%,#9fd0a8 75%,#b9a47c)"></div>
  <p style="top:168px">Vestibulum rutrum pharetra diam, eget dapi-bus leo vehicula ut. Fusce aliquam, odio eget adipiscing lobortis.</p>
  <div class="more" style="top:218px">More info</div>
</div>
<div class="abs card" style="left:377px">
  <div class="ribbon" style="top:18px;background:var(--lime)">DRAINAGE</div>
  <div class="pic" role="img" aria-label="Pipeline running through a forest" style="top:60px;background:linear-gradient(#9cb0ae,#5e7a45 45%,#a7b3a9 70%,#6b6a42)"></div>
  <p style="top:168px">Vestibulum rutrum pharetra diam, eget dapi-bus leo vehicula ut. Fusce aliquam, odio eget adipiscing lobortis.</p>
  <div class="more" style="top:219px">More info</div>
</div>
<div class="abs card" style="left:658px">
  <div class="ribbon" style="top:25px;background:var(--gold)">PUMP STATIONS</div>
  <div class="pic" role="img" aria-label="Workers installing blue pump station valves" style="top:66px;background:linear-gradient(120deg,#a89f90,#3b62b8 50%,#24448f)"></div>
  <p style="top:170px">Vestibulum rutrum pharetra diam, eget dapi-bus leo vehicula ut. Fusce aliquam, odio eget adipiscing lobortis.</p>
  <div class="more" style="top:220px">More info</div>
</div>

<footer>
  <div class="abs footer"></div>
  <div class="abs foot-links">Home - About Us - Pump Stations - Pumps - Electrical - Drainage<br>Environmental - Accessories - Contact Us</div>
  <span class="abs vline" style="left:690px"></span>
  <div class="abs foot-brand"><span class="brand-mark"></span><span class="brand-name">RIVERWELL</span></div>
  <div class="abs footer-bar">
    <span class="copy">Copyright RiverWell 2014. All Rights reserved</span>
    <span class="credit">Website by Pagecraft Studio</span>
  </div>
</footer>

</body>
</html>
```